Business Card Design Project

Professional business cards for law firm - a rough example of what we are looking for is attached. The logo, colour and styling of the name are all new and dont need to be changed. We need layout for front and back. We are looking for some imaginative layout of info. We are a young vibrant firm and not too conservative and are not adverse to something quite different.
Updates

Thank you for all the submissions.  We have been blown away with the quality of your work.  Our management team will be meeting later in the week to make our decision.  Again, thanks for the fabulous work.

Industry/Entity Type

Conservative

Requirements
Must have
• Logo and name as in attached example (colour and font)
Should not have
• Scales of Justice

```html
<!DOCTYPE html>
<html lang="en">
<head>
<meta charset="utf-8">
<title>Fletcher Vale Legal – Business Cards</title>
<link rel="stylesheet" href="https://fonts.googleapis.com/css2?family=Ubuntu:wght@400;500&family=Open+Sans:ital,wght@0,400;0,700;1,400&display=swap">
<style>
  :root {
    --backdrop: #e9e1d4;
    --card: #000000;
    --green: #6a8139;
    --white: #ffffff;
    --text: #e6e6e6;
    --muted: #7e7e7e;
    --ring: #5c5c5c;
  }
  * { margin: 0; padding: 0; box-sizing: border-box; }
  html, body { width: 1200px; height: 402px; overflow: hidden; }
  body {
    background: var(--backdrop);
    position: relative;
    font-family: "Open Sans", Arial, sans-serif;
  }
  .card {
    position: absolute;
    top: 46px;
    width: 524px;
    height: 298px;
    border-radius: 24px;
    background: var(--card);
    overflow: hidden;
  }
  .card--front { left: 54px; }
  .card--back { left: 601px; }
  .card__wave { position: absolute; left: 0; top: 0; width: 524px; height: 298px; }

  .firm-name {
    position: absolute;
    font-family: "Ubuntu", Arial, sans-serif;
    font-weight: 500;
    color: var(--green);
    text-align: center;
    line-height: 1;
  }
  .firm-name__main { display: block; font-size: 30px; }
  .firm-name__sub { display: block; font-size: 16px; letter-spacing: 3px; margin-top: 7px; }
  .card--front .firm-name { left: 0; width: 524px; top: 16px; }
  .card--back .firm-name { left: 240px; width: 206px; top: 84px; }

  .tagline {
    position: absolute;
    font-style: italic;
    font-size: 12px;
    color: var(--muted);
    white-space: nowrap;
  }
  .card--front .tagline { left: 0; width: 524px; text-align: center; top: 90px; }
  .card--back .tagline { left: 252px; top: 153px; }

  .services {
    position: absolute;
    top: 128px;
    list-style: none;
    font-size: 11px;
    line-height: 18.5px;
    color: var(--text);
  }
  .services--left { left: 20px; }
  .services--right { left: 120px; width: 124px; text-align: right; }

  .divider {
    position: absolute;
    left: 264px;
    top: 130px;
    width: 1px;
    height: 82px;
    background: var(--text);
  }
  .contact {
    position: absolute;
    left: 280px;
    top: 127px;
    list-style: none;
    font-size: 11px;
    line-height: 14px;
    color: var(--text);
    white-space: nowrap;
  }
  .contact li { display: flex; align-items: center; gap: 6px; margin-bottom: 4px; }
  .contact li.contact__address { display: block; }
  .contact svg { width: 10px; height: 10px; fill: var(--text); flex: none; }

  .brand-mark {
    position: absolute;
    left: 89px;
    top: 39px;
    width: 140px;
    height: 140px;
    border-radius: 50%;
    border: 3px solid var(--ring);
  }
  .person {
    position: absolute;
    right: 32px;
    top: 252px;
    text-align: center;
    color: var(--white);
  }
  .person__name { font-weight: 700; font-size: 13px; }
  .person__role { font-size: 10px; margin-top: 3px; }
</style>
</head>
<body>

<section class="card card--front">
  <div class="firm-name">
    <span class="firm-name__main">Fletcher Vale</span>
    <span class="firm-name__sub">LEGAL</span>
  </div>
  <p class="tagline">clear advice for every next step</p>

  <ul class="services services--left">
    <li>Family</li>
    <li>Restraining Orders</li>
    <li>Wills &amp; Probate</li>
    <li>Dividing Fences</li>
  </ul>
  <ul class="services services--right">
    <li>Civil</li>
    <li>Debt Recovery</li>
    <li>Criminal &amp; Traffic</li>
    <li>Financial Agreements</li>
  </ul>

  <div class="divider"></div>

  <ul class="contact">
    <li class="contact__address">7/42 Harlow Street, Redcliffe WA 6110<br>PO Box 319, Redcliffe WA 6990</li>
    <li><svg viewBox="0 0 10 10"><path d="M2 0.5 L3.6 0.5 L4.2 2.8 L3.1 3.7 C3.7 5 4.9 6.2 6.2 6.8 L7.1 5.8 L9.5 6.4 L9.5 8 C9.5 9 8.7 9.6 7.8 9.5 C4 9 1 6 0.5 2.2 C0.4 1.3 1 0.5 2 0.5 Z"/></svg>9312 4470, 6255 0836</li>
    <li><svg viewBox="0 0 10 10"><rect x="2.5" y="0.5" width="5" height="3"/><rect x="0.5" y="4" width="9" height="4.5" rx="1"/><rect x="2.5" y="7" width="5" height="2.5"/></svg>6208 5519</li>
    <li><svg viewBox="0 0 10 10"><path d="M0.5 2 H9.5 V8.5 H0.5 Z M0.8 2.3 L5 5.5 L9.2 2.3" stroke="#000" stroke-width="0.6"/></svg>reception@fletchervalelegal.com.au</li>
  </ul>

  <svg class="card__wave" viewBox="0 0 524 298" aria-hidden="true">
    <path d="M0 252 C160 258 350 240 524 226 V298 H0 Z" fill="var(--green)"/>
    <path d="M0 260 C150 265 300 256 400 238 C300 270 190 294 130 300 L0 300 Z" fill="var(--card)"/>
    <path d="M0 271 C140 275 270 264 350 244 C270 272 150 286 0 288 Z" fill="var(--white)"/>
  </svg>
</section>

<section class="card card--back">
  <div class="brand-mark" role="img" aria-label="Fletcher Vale Legal emblem"></div>
  <div class="firm-name">
    <span class="firm-name__main">Fletcher Vale</span>
    <span class="firm-name__sub">LEGAL</span>
  </div>
  <p class="tagline">clear advice for every next step</p>

  <svg class="card__wave" viewBox="0 0 524 298" aria-hidden="true">
    <path d="M0 252 C160 258 350 240 524 226 V298 H0 Z" fill="var(--green)"/>
    <path d="M0 260 C150 265 300 256 400 238 C300 270 190 294 130 300 L0 300 Z" fill="var(--card)"/>
    <path d="M0 271 C140 275 270 264 350 244 C270 272 150 286 0 288 Z" fill="var(--white)"/>
  </svg>

  <div class="person">
    <p class="person__name">Eleanor Fletcher LLB BA</p>
    <p class="person__role">Solicitor</p>
  </div>
</section>

</body>
</html>
```